Veltrion Knowledge Enhancement Company Website

Veltrion is knowledge enhancement Highend and Deep Technology Company who has training programs in Applied Quantum, Applied Artificial Intelligence and Data Science. All the technologies are very advanced and future technologies and the website should reflect the technology advancement. Looking for a sophisticated web design which will reflect our focus on deep and future technologies. Logo file is uploaded

Target Market(s)

Big Corporates and Premium Colleges

Industry/Entity Type

Technology, Deep Technology, Future Technology

Coding

Coded - Design and coding required

Number of Pages Required

5+ page

Requirements
Must have
• A Very Contemporary clean look and should reflect Future Technologies
Nice to have
• Should be very Classy
Should not have
• Traditional Fonts and Colors

```html
<!DOCTYPE html>
<html lang="en">
<head>
<meta charset="utf-8">
<title>Veltrion – The Workforce of the Future</title>
<link rel="stylesheet" href="https://fonts.googleapis.com/css2?family=Exo+2:wght@600;700&family=Heebo:wght@400;500&display=swap">
<style>
:root{
  --bg-deep:#03132a;
  --bg-main:#05193a;
  --bg-story:#061a36;
  --accent:#29abe2;
  --accent-soft:#3ab0e8;
  --text:#ffffff;
  --text-soft:#e6eef7;
}
*{margin:0;padding:0;box-sizing:border-box}
html,body{width:1200px;height:3102px;overflow:hidden;background:var(--bg-main)}
body{position:relative;font-family:'Heebo',sans-serif;color:var(--text)}
.heading{font-family:'Exo 2',sans-serif;font-weight:700;color:var(--text);letter-spacing:-.5px}
.abs{position:absolute}

/* hero */
.hero{position:absolute;left:0;top:0;width:1200px;height:720px;background:linear-gradient(180deg,#03132a 0%,#04183a 70%,#061a36 100%)}
.hero-art{position:absolute;left:0;top:0;width:1200px;height:720px;
  background:
    radial-gradient(ellipse 190px 120px at 1010px 470px,rgba(10,35,70,.9),transparent 75%),
    radial-gradient(ellipse 360px 360px at 1040px 420px,rgba(28,80,128,.75),transparent 72%),
    radial-gradient(ellipse 300px 60px at 760px 390px,rgba(60,170,240,.55),transparent 75%),
    radial-gradient(ellipse 380px 70px at 330px 470px,rgba(45,140,220,.45),transparent 75%),
    radial-gradient(ellipse 700px 140px at 600px 430px,rgba(30,100,180,.35),transparent 70%),
    linear-gradient(165deg,transparent 40%,rgba(40,130,210,.18) 55%,transparent 68%)}
.brand{display:flex;align-items:center;gap:10px;font-family:'Heebo',sans-serif;font-weight:500;color:var(--accent)}
.brand-mark{background:var(--accent)}
.site-brand{left:108px;top:38px;font-size:26px}
.site-brand .brand-mark{width:26px;height:26px}
.nav{position:absolute;display:flex;font-size:15.5px}
.nav a{color:var(--text);text-decoration:none}
.nav a.active{color:var(--accent-soft)}
.top-nav{top:42px;left:446px}
.top-nav a{margin-right:36px}
.top-nav a:last-child{margin-right:0}
.hero-title{left:108px;top:226px;font-size:44px;line-height:53px;width:460px}
.hero-lead{left:111px;top:339px;width:420px;font-size:15.5px;line-height:26px}

/* story */
.story{position:absolute;left:0;top:720px;width:1200px;height:691px;background:var(--bg-story)}
.story-title{position:absolute;left:0;width:1200px;top:34px;text-align:center;font-size:38px}
.story-body{position:absolute;left:150px;top:108px;width:900px;text-align:center;font-size:15.5px;line-height:25.8px;color:var(--text-soft)}
.story-body p{margin-bottom:25.8px}

/* advantage */
.advantage{position:absolute;left:0;top:1411px;width:1200px;height:582px;background:#041630}
.advantage-art{position:absolute;left:500px;top:0;width:700px;height:582px;
  background:radial-gradient(ellipse 260px 200px at 520px 180px,rgba(60,170,220,.45),transparent 70%),
             radial-gradient(ellipse 300px 160px at 200px 150px,rgba(40,110,170,.35),transparent 70%),
             linear-gradient(90deg,#041630 0%,#0c2c4e 45%,#2a4460 100%)}
.advantage-title{left:108px;top:83px;font-size:38px}
.advantage-body{left:108px;top:145px;width:545px;font-size:15.5px;line-height:30px}
.advantage-body p{margin-bottom:30px}

/* training */
.training{position:absolute;left:0;top:1993px;width:1200px;height:577px;background:var(--bg-main)}
.training-brand{left:92px;top:236px;font-size:62px;gap:18px}
.training-brand .brand-mark{width:56px;height:56px}
.training-title{left:542px;top:164px;font-size:38px}
.training-body{left:545px;top:226px;width:540px;font-size:15.5px;line-height:30px}

/* footer */
.footer{position:absolute;left:0;top:2570px;width:1200px;height:532px;
  background:radial-gradient(ellipse 500px 260px at 1150px 520px,rgba(40,120,160,.5),transparent 70%),
             radial-gradient(ellipse 400px 200px at 150px 480px,rgba(40,100,150,.3),transparent 70%),var(--bg-main)}
.footer-brand{left:0;width:1200px;justify-content:center;top:68px;font-size:40px}
.footer-brand .brand-mark{width:36px;height:36px}
.footer-nav{top:210px;left:0;width:1200px;justify-content:center;gap:28px;font-size:13px}
.contact{position:absolute;top:278px;display:flex;gap:14px;font-size:15.5px;line-height:26px}
.contact-icon{width:46px;height:46px;border-radius:50%;background:var(--accent);flex:none;display:flex;align-items:center;justify-content:center;margin-top:4px}
.copyright{position:absolute;left:0;width:1200px;top:374px;text-align:center;font-size:14px}
.copyright span{color:var(--accent-soft)}
.social{position:absolute;top:432px;left:537px;display:flex;gap:12px}
.social i{display:block;width:33px;height:33px;border-radius:50%;background:var(--accent)}
</style>
</head>
<body>

<header class="hero">
  <div class="hero-art" role="img" aria-label="Glowing blue network of connected points over a deep navy background"></div>
  <div class="abs brand site-brand"><span class="brand-mark"></span>Veltrion</div>
  <nav class="nav top-nav">
    <a class="active" href="#">Home</a><a href="#">About</a><a href="#">Solutions</a><a href="#">Our IPs</a><a href="#">Research</a><a href="#">Contact</a><a href="#">Careers</a><a href="#">News</a>
  </nav>
  <h1 class="abs heading hero-title">THE WORKFORCE OF<br>THE FUTURE</h1>
  <p class="abs hero-lead">Nexqubit Academy is an essential part of Nexqubit, brought to life to educate the future of our workforce, both students and professionals.</p>
</header>

<section class="story">
  <h2 class="heading story-title">OUR STORY</h2>
  <div class="story-body">
    <p>We have a vision to create a quantum future by using quantum principles for engineering solutions to extremely complex problems in computing, communications, sensing, chemistry, cryptography, imaging and mechanics.</p>
    <p>Our work is progressing in the direction to provide the world its first Quantum Internet and as a result create a completely secure internet and communication at immense speed and security.</p>
    <p>We have put together a world class team of research quantum and networking scientists to build this new paradigm of secure communications for commercial customers. Our business goal is to deliver reliable, high quality, cost-effective, efficient, scalable and absolutely secure quantum communication solutions to a global marketplace through our quantum Internet platform and software stack by applying latest state-of-art technology advancements with both private and public participation that will provide most secure, more accessible, affordable, and transparent communication platform to consumers, governments, businesses and start-ups.</p>
    <p>Nexqubit, our subsidiary in India, has been named as one of first and among the top 8 start- ups by Tech Horizon Review, aiming to bring India in the list of few countries with an edge in this emerging field which will have a greater advantage in garnering multi-fold economic growth and dominant leadership to lead the quantum computing race in India.</p>
    <p>Our team consists of bright, energetic and talented people who have a passion for making a difference in the world by helping underserved communities.</p>
  </div>
</section>

<section class="advantage">
  <div class="advantage-art" role="img" aria-label="Hand touching streams of glowing binary data above a tablet"></div>
  <h2 class="abs heading advantage-title">BUILD YOUR ADVANTAGE</h2>
  <div class="abs advantage-body">
    <p>In today's competitive environment, organisations that respond faster to change with better insight and greater precision hold a sustainable advantage. Nexqubit will sustain forever.</p>
    <p>Nexqubit brings continuous innovation to help clients to improve their performance and create lasting value.</p>
    <p>At Veltrion our goal is to train aspirants from academia as well as industry who thrive to demonstrate new skills and gain a step up in their career on new quantum technologies. Mentored by experienced scientists in the field we assure you that you can solve critical business problems. Solutions to these problems optimize critical applications.</p>
  </div>
</section>

<section class="training">
  <div class="abs brand training-brand"><span class="brand-mark"></span>Veltrion</div>
  <h2 class="abs heading training-title">THE BEST TRAINING GROUNDS</h2>
  <p class="abs training-body">We provide best research labs in quantum technologies at Northgate Institute, Riverton Institute, Eastfield Institute and more in the future. We are always looking for partnerships and collaborations to bring best talent on board as mentors for our Veltrion. We create opportunities, across the globe with excellent Quantum platform providers like Orbiton, Cloudvale, Quantix etc.,</p>
</section>

<footer class="footer">
  <div class="abs brand footer-brand"><span class="brand-mark"></span>Veltrion</div>
  <nav class="nav footer-nav">
    <a class="active" href="#">Home</a><a href="#">About</a><a href="#">Solutions</a><a href="#">Our IPs</a><a href="#">Research</a><a href="#">Contact</a><a href="#">Careers</a><a href="#">News</a>
  </nav>
  <div class="contact" style="left:267px">
    <span class="contact-icon"><svg width="16" height="20" viewBox="0 0 16 20"><path d="M8 0a8 8 0 0 0-8 8c0 6 8 12 8 12s8-6 8-12a8 8 0 0 0-8-8zm0 11a3 3 0 1 1 0-6 3 3 0 0 1 0 6z" fill="#fff"/></svg></span>
    <div>Nexqubit Inc<br>4820 Harbor Lane<br>Brackenport Delaware, 19000</div>
  </div>
  <div class="contact" style="left:533px">
    <span class="contact-icon"><svg width="20" height="20" viewBox="0 0 20 20"><path d="M4 1l3 0 2 5-2.5 1.5a11 11 0 0 0 6 6L14 11l5 2v3a3 3 0 0 1-3 3C8 19 1 12 1 4a3 3 0 0 1 3-3z" fill="#fff"/></svg></span>
    <div>Phone<br>+1555 010 0199</div>
  </div>
  <div class="contact" style="left:762px">
    <span class="contact-icon"><svg width="20" height="15" viewBox="0 0 20 15"><rect width="20" height="15" rx="2" fill="#fff"/><path d="M1 2l9 6 9-6" stroke="#29abe2" stroke-width="2" fill="none"/></svg></span>
    <div>Email<br>info@nexqubit.example</div>
  </div>
  <p class="copyright">© copyrights 2023 <span>Veltrion</span> &nbsp;| &nbsp;&nbsp; All rights reserved.</p>
  <div class="social" aria-label="Social links"><i></i><i></i><i></i></div>
</footer>

</body>
</html>
```